Accident Law Firm Billboard Bold Easy to See Car Accidents

We need a billboard design that can catch attention in a very crowed Car Accident lawyer market. We wish to feature the phone number (407) 555-0148 as the focus of the Bill Board. We are trying to get the phone number recognized and remembered by drivers. The law firm name is not as crucial to remember.
Basically, It's CAR ACCIDENT? Then (407) 555-0148. We are not married to any specific color scheme but it has to POP and catch attention.
So the Crucial elements are as follows:
1. Phone number (407) 555-0148
2. Words CAR ACCIDENT?
3. Firm Logo in lower portion or where appropriate. Firm Logo to be provided
4. We may want to try a Day Glow orange color, with White and Black added. An example of the color scheme shall be provided.
5. Possible "Catch Phrase" to be used, "It's Time Call 9"
Target Market(s)
Orlando Florida Car Accident victims
Industry/Entity Type
Law Firm
Requirements
Must have
- Easy to see phone number (407) 555-0148
- Catch attention
Nice to have
- I would like to have the sign visible in bright sunlight and it not too hard to immediately know what phone number is for
Should not have
- too many words
- No bold enough
- confusing fonts
- Unclear fonts

```html
<!DOCTYPE html>
<html lang="en">
<head>
<meta charset="utf-8">
<title>Car Accident Billboard</title>
<link href="https://fonts.googleapis.com/css2?family=Arimo:wght@700&family=Montserrat:wght@700;800&display=swap" rel="stylesheet">
<style>
  :root {
    --backdrop: #2b2d31;
    --signal-red: #d4301d;
    --signal-mid: #dd4a22;
    --signal-orange: #e9782c;
    --headline-white: #f6efe8;
    --firm-ink: #5b2b17;
    --gauge-tone: rgba(255, 235, 220, 0.35);
  }
  * { margin: 0; padding: 0; box-sizing: border-box; }
  html, body {
    width: 1200px;
    height: 800px;
    overflow: hidden;
    background: var(--backdrop);
  }
  .canvas {
    position: relative;
    width: 1200px;
    height: 800px;
    display: flex;
    align-items: center;
    justify-content: center;
  }
  .billboard {
    position: relative;
    width: 1140px;
    height: 380px;
    background:
      radial-gradient(ellipse at 95% 10%, var(--signal-orange) 0%, rgba(233,120,44,0) 55%),
      linear-gradient(90deg, var(--signal-red) 0%, var(--signal-mid) 60%, var(--signal-orange) 100%);
    color: var(--headline-white);
    text-align: center;
  }
  .headline {
    position: absolute;
    top: 44px;
    left: 0;
    width: 100%;
    font-family: "Montserrat", Arial, sans-serif;
    font-weight: 800;
    font-size: 46px;
    letter-spacing: 6px;
    padding-left: 40px;
  }
  .phone-number {
    position: absolute;
    top: 118px;
    left: 0;
    width: 100%;
    font-family: "Arimo", Arial, sans-serif;
    font-weight: 700;
    font-size: 124px;
    line-height: 1;
    letter-spacing: 14px;
  }
  .catch-phrase {
    position: absolute;
    top: 272px;
    left: 0;
    width: 100%;
    font-family: "Montserrat", Arial, sans-serif;
    font-weight: 700;
    font-size: 46px;
    letter-spacing: 4px;
    padding-right: 60px;
  }
  .firm-name {
    position: absolute;
    top: 26px;
    right: 26px;
    font-family: "Montserrat", Arial, sans-serif;
    font-weight: 800;
    font-size: 18px;
    line-height: 1.05;
    letter-spacing: 1px;
    color: var(--firm-ink);
    text-align: left;
    text-transform: uppercase;
  }
  .gauge-area {
    position: absolute;
    right: 4px;
    bottom: 0;
    width: 140px;
    height: 140px;
    border-radius: 140px 140px 0 0;
    background: radial-gradient(circle at 60% 100%, var(--gauge-tone) 0%, rgba(255,235,220,0) 70%);
  }
</style>
</head>
<body>
  <main class="canvas">
    <section class="billboard">
      <h1 class="headline">CAR ACCIDENT?</h1>
      <p class="phone-number">407-555-0148</p>
      <p class="catch-phrase">Why Wait? Dial the 9!</p>
      <p class="firm-name">Marlowe<br>Law Firm P.C.</p>
      <div class="gauge-area" role="img" aria-label="Speedometer gauge illustration"></div>
    </section>
  </main>
</body>
</html>
```